Website design needed for gift based dropship website

I am building a dropshipping website that will create gift based merchandise and send it out to our clients customers for them. Our clients will sell products and when a customer buys from them, we create the item and send it out to the customer.

I am looking for a very similar website to quillmarten.com - that website is doing a very similar thing to what i am doing but where the quillmarten website is based around clothing, my website will be based around gifts. Another website that i like that is doing a similar thing to what i will do is bavrel.com

I require 2 pages to be made:
1) The home page
2) A landing page for a free product giveaway offer

1) THE HOME PAGE
The home page should be a merger of the two previously stated websites (www.bavrel.com and www.quillmarten.com). The style fo the homepage should be based on the logo that is attached and the colour scheme should be similar but basic.

2) THE LANDING PAGE
The landing page will be giving away a free mobile phone cover. The page needs to have some mobile phone covers for different phones all with random designs on. The page should state that they can have any design that they want and they do not pay for the phone (they only pay for shipping).

Menu pages and text should be taken from the quillmarten.com website.

Target Market(s)

18 - 40 year old males. People who like the idea of earning extra money in their spare time but aren't too sure how to do it. Semi-professional jobs.

Number of Pages Required

2 page

Font styles to use
Serif
Sans Serif
Decorative
Script

Colors

Designer to choose colors to be used in the design.

Requirements
Must have
• A "how it works" image where the dropshipping process is explained to a visitor to the website (similar to the one on the quillmarten "how it works page")
Nice to have
• Testimonial area on homepage
Should not have
• Homepage should not have:
• - "latest orders from" area
• - Video
• - Warehousing/fulfilment area
• - Integration area
• -

```html
<!DOCTYPE html>
<html lang="en">
<head>
<meta charset="utf-8">
<title>Merrow Prints – Personalised Gifts</title>
<link href="https://fonts.googleapis.com/css2?family=Open+Sans:wdth,wght@75..100,300..800&display=swap" rel="stylesheet">
<style>
:root{
  --red:#e52421;
  --maroon:#3d0d14;
  --blue:#1eaee8;
  --teal:#2aa7a0;
  --grey:#eeeeee;
  --card-grey:#e9e9e9;
  --dark:#2b2b2b;
  --text:#555555;
  --ink:#222222;
  --white:#ffffff;
}
*{margin:0;padding:0;box-sizing:border-box}
html,body{width:1200px;height:4100px;overflow:hidden}
body{position:relative;background:var(--white);font-family:"Open Sans",Arial,sans-serif;color:var(--text)}
.abs{position:absolute}
.heading{font-family:"Open Sans",Arial,sans-serif;font-stretch:75%;font-weight:700;text-transform:uppercase;text-align:center;position:absolute;left:0;width:1200px}
.heading--teal{color:var(--teal);font-size:46px}
.heading--dark{color:var(--ink);font-size:32px}
.wave{position:absolute;left:0;width:1200px}

/* header */
.site-header{position:absolute;top:0;left:0;width:1200px;height:123px;background:var(--white)}
.brand{position:absolute;left:131px;top:30px;display:flex;align-items:center;gap:12px}
.brand__dot{width:44px;height:44px;border-radius:50%;background:var(--red)}
.brand__name{font-stretch:75%;font-weight:800;font-size:36px;line-height:1;color:var(--maroon);text-transform:uppercase;width:130px}
.account{position:absolute;top:27px;left:888px;display:flex;gap:11px}
.btn{display:inline-flex;align-items:center;justify-content:center;font-stretch:75%;font-weight:700;text-transform:uppercase;color:var(--white);font-size:14px}
.account .btn{height:28px;background:var(--red)}
.nav{position:absolute;top:82px;left:0;width:1200px;height:24px}
.nav a{position:absolute;font-stretch:75%;font-weight:600;font-size:16px;color:var(--ink);text-decoration:none;text-transform:uppercase}
.nav a.is-active{color:var(--red)}

/* hero */
.hero{position:absolute;top:123px;left:0;width:1200px;height:540px;background:linear-gradient(#ffffff,#f7f7f7)}
.hero__cta{position:absolute;top:27px;height:30px;width:169px}
.product{position:absolute;border-radius:10px}
.slider-arrow{position:absolute;top:232px;width:28px;height:28px;background:var(--ink);display:flex;align-items:center;justify-content:center}

/* welcome */
.intro{position:absolute;top:780px;left:131px;width:935px;font-size:13.5px;line-height:24px;text-align:center;color:var(--text)}
.rule{position:absolute;top:902px;left:131px;width:935px;height:1px;background:#dddddd}

/* steps */
.step{position:absolute;top:1011px;width:295px;height:205px;color:var(--white);text-align:center}
.step__icon{position:absolute;top:28px;left:115px;width:66px;height:66px}
.step__label{position:absolute;top:126px;left:20px;width:255px;font-stretch:75%;font-weight:700;font-size:19px;line-height:26px;text-transform:uppercase}
.step--red{left:131px;background:var(--red)}
.step--maroon{left:451px;background:var(--maroon)}
.step--blue{left:771px;background:var(--blue)}
.step-arrow{position:absolute;top:1026px;width:60px;height:34px}

.feature{position:absolute;top:1279px;width:451px;height:260px;background:var(--card-grey);text-align:center}
.feature__icon{position:absolute;top:30px;left:193px;width:66px;height:80px}
.feature__title{position:absolute;top:118px;left:0;width:451px;font-stretch:75%;font-weight:700;font-size:32px;color:var(--ink);text-transform:uppercase}
.feature__text{position:absolute;top:170px;left:45px;width:361px;font-size:10.5px;line-height:16px;color:var(--text)}

/* gifts */
.gifts{position:absolute;top:1640px;left:0;width:1200px;height:890px;background:var(--grey)}
.gift{position:absolute;width:293px;height:243px;background:var(--white);box-shadow:0 1px 3px rgba(0,0,0,.12)}
.gift__photo{position:absolute;top:22px;left:66px;width:161px;height:150px;border-radius:8px}
.gift__name{position:absolute;top:199px;left:0;width:293px;text-align:center;font-stretch:75%;font-weight:700;font-size:19px;color:var(--ink);text-transform:uppercase}
.read-more{position:absolute;top:732px;left:542px;width:116px;height:41px;background:var(--red)}

/* testimonials */
.quote{position:absolute;top:2678px;left:163px;width:874px;font-size:16.5px;line-height:28px;text-align:center;color:var(--text)}
.quote__author{position:absolute;top:2775px;left:0;width:1200px;text-align:center;font-stretch:75%;font-weight:700;font-size:14px;color:var(--ink);text-transform:uppercase}
.stars{position:absolute;top:2797px;left:553px;width:94px;height:18px}
.chevron{position:absolute;top:2725px;width:20px;height:30px}

/* difference */
.difference{position:absolute;top:2930px;left:0;width:1200px;height:520px;background:var(--grey)}
.point{position:absolute;width:300px;text-align:center}
.point__tick{display:block;margin:0 auto;width:38px;height:38px}
.point__title{margin-top:6px;font-stretch:75%;font-weight:700;font-size:19px;color:var(--maroon)}
.point__text{margin-top:4px;font-size:10.5px;line-height:15px;color:var(--text)}

/* contact */
.contact-band{position:absolute;top:3420px;left:0;width:1200px;height:311px}
.contact__title{position:absolute;top:3558px;color:var(--white);font-size:50px}
.contact__line{position:absolute;top:3626px;left:0;width:1200px;text-align:center;color:var(--red);font-weight:600;font-size:17px}
.contact__line span{margin:0 12px}
.contact__line svg{vertical-align:-2px;margin-right:6px}

/* footer */
.site-footer{position:absolute;top:3731px;left:0;width:1200px;height:369px;background:var(--white)}
.footer-brand{position:absolute;left:131px;top:104px;display:flex;align-items:center;gap:10px}
.footer-col{position:absolute;top:46px;padding-left:22px;border-left:1px solid #dddddd;height:190px}
.footer-col h4{font-stretch:75%;font-weight:700;font-size:17px;color:var(--ink);text-transform:uppercase;margin-bottom:16px}
.footer-col li{list-style:none;font-size:11.5px;line-height:27px;color:var(--text)}
.footer-rule{position:absolute;top:259px;left:131px;width:935px;height:1px;background:#dddddd}
.copyright{position:absolute;top:288px;left:131px;font-size:11px;color:var(--text)}
.social{position:absolute;top:278px;left:902px;display:flex;gap:11px}
.social span{width:34px;height:34px;border-radius:50%;border:1.5px solid var(--red)}
</style>
</head>
<body>

<header class="site-header">
  <div class="brand">
    <span class="brand__dot"></span>
    <span class="brand__name">Merrow Prints</span>
  </div>
  <div class="account">
    <span class="btn" style="width:77px">Log In</span>
    <span class="btn" style="width:90px">Register</span>
  </div>
  <nav class="nav">
    <a class="is-active" style="left:661px">Home</a>
    <a style="left:738px">About Us</a>
    <a style="left:838px">Services</a>
    <a style="left:934px">Team</a>
    <a style="left:1008px">Contact</a>
  </nav>
</header>

<section class="hero">
  <span class="btn hero__cta" style="left:424px;background:var(--maroon)">Browse Products</span>
  <span class="btn hero__cta" style="left:607px;background:var(--blue)">Upload Photo for Print</span>

  <div class="product" role="img" aria-label="Grey ceramic mug" style="left:77px;top:123px;width:210px;height:246px;background:linear-gradient(135deg,#d4d4d4,#9a9a9a)"></div>
  <div class="product" role="img" aria-label="Grey metal water bottle" style="left:333px;top:128px;width:82px;height:241px;background:linear-gradient(90deg,#bdbdbd,#8c8c8c,#bdbdbd)"></div>
  <div class="product" role="img" aria-label="Red backpack with printed photo" style="left:451px;top:68px;width:205px;height:438px;border-radius:40px;background:linear-gradient(160deg,#ee3a33,#b81616)"></div>
  <div class="product" role="img" aria-label="Grey baseball cap" style="left:705px;top:137px;width:252px;height:232px;border-radius:120px 120px 20px 20px;background:linear-gradient(135deg,#cfcfcf,#9d9d9d)"></div>
  <div class="product" role="img" aria-label="Grey phone case" style="left:1006px;top:145px;width:123px;height:224px;border-radius:14px;background:linear-gradient(135deg,#c6c6c6,#8f8f8f)"></div>

  <div class="slider-arrow" style="left:0"><svg width="12" height="12" viewBox="0 0 12 12"><path d="M8 1 3 6l5 5" fill="none" stroke="#fff" stroke-width="2"/></svg></div>
  <div class="slider-arrow" style="left:1172px"><svg width="12" height="12" viewBox="0 0 12 12"><path d="M4 1l5 5-5 5" fill="none" stroke="#fff" stroke-width="2"/></svg></div>
</section>

<svg class="wave" style="top:570px" height="110" viewBox="0 0 1200 110" preserveAspectRatio="none">
  <path d="M0 60 C250 30 500 40 720 85 C900 110 1080 70 1200 20 L1200 110 L0 110Z" fill="#fff"/>
  <path d="M0 58 C250 28 500 38 720 83 C900 108 1080 68 1200 18" fill="none" stroke="var(--red)" stroke-width="7"/>
  <path d="M0 66 C260 36 500 50 720 92 C900 116 1080 78 1200 30" fill="none" stroke="var(--blue)" stroke-width="6"/>
</svg>

<h2 class="heading heading--teal" style="top:712px">Welcome</h2>
<p class="intro">Aenean facilisis tincidunt lectus, id dictum nisi luctus eget. Vivamus efficitur ex condimentum, malesuada eros eget, feugiat nibh. Sed tellus ex, imperdiet eget gravida sit amet, volutpat eget turpis. In nec ultricies est. Etiam mattis augue vehicula odio posuere, sit amet tempus lectus luctus. Nulla facilisi. Etiam vel massa elementum, bibendum tellus venenatis, feugiat massa. Curabitur venenatis lacinia ornare. Cras sollicitudin quis dui eu placerat.</p>
<div class="rule"></div>

<h2 class="heading heading--dark" style="top:954px">How It Works</h2>

<div class="step step--red">
  <svg class="step__icon" viewBox="0 0 66 66" fill="none" stroke="#fff" stroke-width="3"><rect x="6" y="10" width="46" height="50"/><path d="M22 44l4-12 26-26 8 8-26 26z"/></svg>
  <div class="step__label">Sign up with us and choose product for print</div>
</div>
<div class="step step--maroon">
  <svg class="step__icon" viewBox="0 0 66 66" fill="none" stroke="#fff" stroke-width="3"><path d="M4 18h20l5 6h33v34H4z"/><path d="M12 24V10h40v14"/><path d="M18 16h28"/></svg>
  <div class="step__label">Upload your photo and confirm order</div>
</div>
<div class="step step--blue">
  <svg class="step__icon" viewBox="0 0 66 66" fill="none" stroke="#fff" stroke-width="3"><rect x="6" y="8" width="54" height="14"/><rect x="10" y="22" width="46" height="36"/><path d="M26 32h14"/></svg>
  <div class="step__label">Get your product on free shipping</div>
</div>
<svg class="step-arrow" style="left:402px" viewBox="0 0 60 34" fill="none" stroke="#fff" stroke-width="3"><path d="M4 28C14 8 38 4 52 16"/><path d="M44 16h9V7"/></svg>
<svg class="step-arrow" style="left:722px" viewBox="0 0 60 34" fill="none" stroke="#fff" stroke-width="3"><path d="M4 28C14 8 38 4 52 16"/><path d="M44 16h9V7"/></svg>

<div class="feature" style="left:131px">
  <svg class="feature__icon" viewBox="0 0 66 80" fill="var(--red)"><circle cx="33" cy="22" r="17"/><path d="M4 78c0-20 12-34 29-34s29 14 29 34z"/></svg>
  <div class="feature__title">Vestibulum</div>
  <p class="feature__text">Fusce sollicitudin lorem et luctus volutpat. Proin placerat dapibus gravida. In tristique tristique nulla eget hendrerit. Maecenas vel tortor accumsan quam varius imperdiet vel eget elit. Aenean facilisis tincidunt lectus.</p>
</div>
<div class="feature" style="left:615px">
  <svg class="feature__icon" viewBox="0 0 66 80" fill="var(--red)"><rect x="8" y="6" width="50" height="8"/><path d="M4 16h58l-4 18H8z"/><rect x="8" y="36" width="50" height="40"/><rect x="16" y="48" width="14" height="28" fill="#e9e9e9"/><rect x="36" y="46" width="14" height="12" fill="#e9e9e9"/></svg>
  <div class="feature__title">Curabitur</div>
  <p class="feature__text">Fusce sollicitudin lorem et luctus volutpat. Proin placerat dapibus gravida. In tristique tristique nulla eget hendrerit. Maecenas vel tortor accumsan quam varius imperdiet vel eget elit. Aenean facilisis tincidunt lectus.</p>
</div>

<section class="gifts">
  <h2 class="heading heading--teal" style="top:100px">Gift Items</h2>
  <div class="gift" style="left:131px;top:186px"><div class="gift__photo" role="img" aria-label="Black cap" style="background:linear-gradient(135deg,#444,#111)"></div><div class="gift__name">Caps</div></div>
  <div class="gift" style="left:454px;top:186px"><div class="gift__photo" role="img" aria-label="Canvas tote bag" style="background:linear-gradient(135deg,#e6e2d6,#c8c2b0)"></div><div class="gift__name">Bags</div></div>
  <div class="gift" style="left:773px;top:186px"><div class="gift__photo" role="img" aria-label="Coloured wrist bands" style="background:linear-gradient(135deg,#f4c21a,#e0457a,#2e56a8)"></div><div class="gift__name">Wrist Band</div></div>
  <div class="gift" style="left:131px;top:459px"><div class="gift__photo" role="img" aria-label="Grey and red laptop bag" style="background:linear-gradient(135deg,#6b6b7a,#3c3c48)"></div><div class="gift__name">Laptop Bags</div></div>
  <div class="gift" style="left:454px;top:459px"><div class="gift__photo" role="img" aria-label="Striped coffee mug" style="background:linear-gradient(135deg,#3ec3d6,#e5d63a)"></div><div class="gift__name">Coffee Mugs</div></div>
  <div class="gift" style="left:773px;top:459px"><div class="gift__photo" role="img" aria-label="Blue notebook" style="background:linear-gradient(135deg,#5466e8,#2a36b0)"></div><div class="gift__name">Notebook</div></div>
  <span class="btn read-more">Read More</span>
</section>

<svg class="wave" style="top:2470px" height="100" viewBox="0 0 1200 100" preserveAspectRatio="none">
  <path d="M0 0H1200V20 C1000 50 800 80 560 70 C340 62 150 40 0 70Z" fill="var(--grey)"/>
  <path d="M0 70 C150 40 340 62 560 70 C800 80 1000 50 1200 20" fill="none" stroke="var(--red)" stroke-width="7"/>
  <path d="M0 80 C150 50 340 72 560 80 C800 90 1000 60 1200 32" fill="none" stroke="var(--blue)" stroke-width="6"/>
</svg>

<h2 class="heading heading--teal" style="top:2616px">Testimonials</h2>
<svg class="chevron" style="left:55px" viewBox="0 0 20 30"><path d="M15 3 4 15l11 12" fill="none" stroke="#999" stroke-width="2"/></svg>
<svg class="chevron" style="left:1125px" viewBox="0 0 20 30"><path d="M5 3l11 12L5 27" fill="none" stroke="#999" stroke-width="2"/></svg>
<p class="quote">“ Vivamus efficitur ex condimentum, malesuada eros eget, feugiat nibh. Sed tellus ex, imperdiet eget gravida sit amet, volutpat eget turpis. In nec ultricies est. Etiam mattis augue vehicula odio posuere, sit amet tempus lectus luctus. Nulla facilisi. Etiam vel massa elementum, bibendum tellus venenatis, feugiat massa. ”</p>
<div class="quote__author">Daniel Rusk, City</div>
<svg class="stars" viewBox="0 0 94 18" fill="var(--red)">
  <path id="star" d="M9 0l2.6 5.8 6.4.6-4.8 4.3 1.4 6.3L9 13.8 3.4 17l1.4-6.3L0 6.4l6.4-.6z"/>
  <use href="#star" x="19"/><use href="#star" x="38"/><use href="#star" x="57"/><use href="#star" x="76"/>
</svg>

<section class="difference">
  <h2 class="heading heading--teal" style="top:86px">What Makes Us Different</h2>
  <div class="point" style="left:129px;top:182px"><svg class="point__tick" viewBox="0 0 38 38"><circle cx="19" cy="19" r="19" fill="var(--red)"/><path d="M10 19l6 6 12-12" fill="none" stroke="#fff" stroke-width="4"/></svg><div class="point__title">Aliquam erat volutpat</div><p class="point__text">Quisque aliquet ex nec est vestibulum pulvinar. Pellentesque convallis molestie enim sit amet efficitur. Etiam id imperdiet luctus.</p></div>
  <div class="point" style="left:450px;top:182px"><svg class="point__tick" viewBox="0 0 38 38"><circle cx="19" cy="19" r="19" fill="var(--red)"/><path d="M10 19l6 6 12-12" fill="none" stroke="#fff" stroke-width="4"/></svg><div class="point__title">Proin a mauris</div><p class="point__text">Quisque aliquet ex nec est vestibulum pulvinar. Pellentesque convallis molestie enim sit amet efficitur. Etiam id imperdiet luctus.</p></div>
  <div class="point" style="left:771px;top:182px"><svg class="point__tick" viewBox="0 0 38 38"><circle cx="19" cy="19" r="19" fill="var(--red)"/><path d="M10 19l6 6 12-12" fill="none" stroke="#fff" stroke-width="4"/></svg><div class="point__title">Vestibulum eget nisl</div><p class="point__text">Quisque aliquet ex nec est vestibulum pulvinar. Pellentesque convallis molestie enim sit amet efficitur. Etiam id imperdiet luctus.</p></div>
  <div class="point" style="left:129px;top:348px"><svg class="point__tick" viewBox="0 0 38 38"><circle cx="19" cy="19" r="19" fill="var(--red)"/><path d="M10 19l6 6 12-12" fill="none" stroke="#fff" stroke-width="4"/></svg><div class="point__title">Aenean sed quam</div><p class="point__text">Quisque aliquet ex nec est vestibulum pulvinar. Pellentesque convallis molestie enim sit amet efficitur. Etiam id imperdiet luctus.</p></div>
  <div class="point" style="left:450px;top:348px"><svg class="point__tick" viewBox="0 0 38 38"><circle cx="19" cy="19" r="19" fill="var(--red)"/><path d="M10 19l6 6 12-12" fill="none" stroke="#fff" stroke-width="4"/></svg><div class="point__title">Praesent quis</div><p class="point__text">Quisque aliquet ex nec est vestibulum pulvinar. Pellentesque convallis molestie enim sit amet efficitur. Etiam id imperdiet luctus.</p></div>
  <div class="point" style="left:771px;top:348px"><svg class="point__tick" viewBox="0 0 38 38"><circle cx="19" cy="19" r="19" fill="var(--red)"/><path d="M10 19l6 6 12-12" fill="none" stroke="#fff" stroke-width="4"/></svg><div class="point__title">Aenean faucibus</div><p class="point__text">Quisque aliquet ex nec est vestibulum pulvinar. Pellentesque convallis molestie enim sit amet efficitur. Etiam id imperdiet luctus.</p></div>
</section>

<svg class="wave" style="top:2860px" height="100" viewBox="0 0 1200 100" preserveAspectRatio="none">
  <path d="M0 40 C200 80 420 85 640 60 C860 36 1040 20 1200 50 L1200 100 L0 100Z" fill="var(--grey)"/>
  <path d="M0 24 C200 64 420 70 640 46 C860 22 1040 6 1200 36" fill="none" stroke="var(--blue)" stroke-width="6"/>
  <path d="M0 38 C200 78 420 84 640 59 C860 35 1040 19 1200 49" fill="none" stroke="var(--red)" stroke-width="7"/>
</svg>

<svg class="contact-band" viewBox="0 0 1200 311" preserveAspectRatio="none" aria-hidden="true">
  <path d="M0 30 C250 110 600 110 900 70 C1030 52 1130 50 1200 70 L1200 311 L0 311Z" fill="var(--dark)"/>
</svg>
<h2 class="heading contact__title">Contact Us</h2>
<div class="contact__line">
  <span><svg width="16" height="16" viewBox="0 0 16 16" fill="var(--red)"><path d="M3 1l3 3-2 2c1 2 3 4 5 5l2-2 3 3-2 3C7 15 1 9 1 3z"/></svg>465 555 0192</span>|<span><svg width="16" height="14" viewBox="0 0 16 14" fill="var(--red)"><path d="M0 1h16v2L8 8 0 3z"/><path d="M0 5l8 5 8-5v9H0z"/></svg>info@merrowprints.com</span>
</div>

<footer class="site-footer">
  <div class="footer-brand">
    <span class="brand__dot" style="width:38px;height:38px"></span>
    <span class="brand__name" style="font-size:32px;width:115px">Merrow Prints</span>
  </div>
  <div class="footer-col" style="left:418px">
    <h4>Information</h4>
    <ul><li>About Us</li><li>Careers</li><li>Privacy &amp; Security</li><li>Site Map</li><li>Terms of Use</li><li>Blog</li></ul>
  </div>
  <div class="footer-col" style="left:656px">
    <h4>Help &amp; Support</h4>
    <ul><li>Recommended Reading</li><li>Submit your Story</li><li>Contact Us</li><li>Frequently Asked Questions</li><li>How to Order</li></ul>
  </div>
  <div class="footer-col" style="left:896px">
    <h4>My Account</h4>
    <ul><li>Delivery Information</li><li>My Account</li><li>Order Tracking</li><li>Reminder Service</li><li>Shipping, Returns &amp; Fees</li></ul>
  </div>
  <div class="footer-rule"></div>
  <p class="copyright">Copyright © 2016, Merrow Prints. All Rights Reserved.</p>
  <div class="social"><span></span><span></span><span></span><span></span></div>
</footer>

</body>
</html>
```